Norvale Email Signature Banners – Fabrication Capability Series

www.Norvale.com.au is an Australian engineering and fabrication company specialising in fabrication and welding of :
steel piping spools,
skids and frames,
small volume process steel tanks
and general steel fabrication
We require four distinct banner designs for use in Teldrin Quillmark email signatures. Each banner will highlight a specific capability while maintaining a consistent brand identity.
Deliverables
Four banners total:
Piping Spools Fabrication – focus on precision welding and stainless steel pipework
Skid & Frames Fabrication – highlight skid systems and structural frames
Small Steel Tanks Fabrication – show fabricated tanks and workshop craftsmanship
General Fabrication Solutions – broad steel fabrication theme for company-wide use
Dimensions: 600–700 px wide × 100 px high
Format: PNG (preferred), small file size prefered
Resolution: 72 dpi
Background: non-transparent, industrial or workshop setting
Text examples:
1. Piping Spools Fabrication
Option A: “Expert Fabrication Solutions for Process Piping”
Option B: “Precision Welding for Complex Systems”
Option C: “Delivering Quality in Every Spool”
Option D: “Engineered for Flow, Built for Strength”
2. Skid & Frames Fabrication
Option A: “Custom Engineered Modular Systems”
Option B: “Built Strong. Designed Smart.”
Option C: “Reliable Frames for Industrial Performance”
Option D: “Modular Fabrication for Seamless Integration”
3. Small Steel Tanks Fabrication
Option A: “Precision Built for Your Needs”
Option B: “Compact Strength. Proven Durability.”
Option C: “Fabricated for Performance and Longevity”
Option D: “Small Tanks. Big Reliability.”
4. General Fabrication Solutions
Option A: “Quality Craftsmanship, Proven Results”
Option B: “Your Partner in Precision Fabrication”
Option C: “Engineering Excellence in Every Weld”
Option D: “Australian Fabrication. Global Standards.”
Style Direction
Clean, professional, and engineering‑focused
Use Norvale brand colours
Blend photo realism with vector clarity (no heavy gradients)
Include subtle industrial textures or workshop imagery
Typography: bold sans‑serif, legible at small scale
Usage Context
These banners will appear at the bottom of staff email signatures via Quillmark Email Signature Tool for Teldrin 365, so clarity and fast loading are essential. No Logo is required in the banners.
Reference
Existing Norvale signature is attached. Colour palette to match the signature style and logo.
Target Market(s)
Engineering and construction companies,
Industry/Entity Type
Engineering fabrication design

```html
<!DOCTYPE html>
<html lang="en">
<head>
<meta charset="utf-8">
<title>Norvale – Piping Spools Signature Banner</title>
<link rel="stylesheet" href="https://fonts.googleapis.com/css2?family=Saira:ital,wght@1,500;1,700&display=swap">
<style>
  :root {
    --page-bg: #f2f2f4;
    --brand-blue: #22a8e0;
    --edge-dark: #1e1e1e;
    --photo-dark: #141414;
    --photo-mid: #3a3a3c;
    --steel-light: #e6e6e8;
    --steel-mid: #9a9a9e;
    --text-light: #ffffff;
  }
  html, body {
    margin: 0;
    padding: 0;
    width: 1200px;
    height: 1200px;
    overflow: hidden;
    background: var(--page-bg);
  }
  .banner {
    position: absolute;
    left: 204px;
    top: 535px;
    width: 792px;
    height: 132px;
    box-shadow: 4px 5px 6px rgba(0,0,0,0.35);
  }
  .banner-shapes {
    position: absolute;
    inset: 0;
    display: block;
  }
  .banner-headline {
    position: absolute;
    left: 382px;
    margin: 0;
    font-family: "Saira", "Arial Narrow", sans-serif;
    font-style: italic;
    color: var(--text-light);
    white-space: nowrap;
    line-height: 1;
  }
  .headline-main {
    top: 24px;
    font-size: 36px;
    font-weight: 700;
    letter-spacing: -0.2px;
  }
  .headline-sub {
    top: 66px;
    font-size: 35px;
    font-weight: 500;
  }
</style>
</head>
<body>
  <div class="banner">
    <svg class="banner-shapes" width="792" height="132" viewBox="0 0 792 132" xmlns="http://www.w3.org/2000/svg">
      <defs>
        <radialGradient id="photoTone" cx="0.45" cy="0.5" r="0.7">
          <stop offset="0" stop-color="var(--photo-mid)" style="stop-color:#3a3a3c"/>
          <stop offset="1" stop-color="var(--photo-dark)" style="stop-color:#141414"/>
        </radialGradient>
        <linearGradient id="steelStrip" x1="0" y1="0" x2="1" y2="1">
          <stop offset="0" style="stop-color:#e6e6e8"/>
          <stop offset="1" style="stop-color:#9a9a9e"/>
        </linearGradient>
      </defs>
      <g class="photo-area" role="img" aria-label="Photograph of stacked stainless steel pipes in a dark workshop">
        <polygon points="0,0 383,0 332,132 0,132" fill="url(#photoTone)"/>
      </g>
      <polygon class="steel-strip" points="367,0 383,0 332,132 316,132" fill="url(#steelStrip)"/>
      <polygon class="blue-panel" points="383,0 780,0 780,132 332,132" fill="#22a8e0"/>
      <rect class="edge-strip" x="780" y="0" width="12" height="132" fill="#1e1e1e"/>
    </svg>
    <p class="banner-headline headline-main">PRECISION WELDING</p>
    <p class="banner-headline headline-sub">for Complex Systems</p>
  </div>
</body>
</html>
```